Marbleton Health group for a medical office

We need a website created that for our new medical office that will support online booking for appointments. You designed the logo already.

```html
<!DOCTYPE html>
<html lang="en">
<head>
<meta charset="utf-8">
<title>Marbleton Health Group</title>
<link href="https://fonts.googleapis.com/css2?family=Inter:wght@300;400;500;600;700;800&family=Roboto:wght@400;500;700&display=swap" rel="stylesheet">
<style>
:root{
  --navy:#163e63;
  --navy-deep:#123658;
  --teal:#2ba3a5;
  --teal-dark:#1e8c8f;
  --ice:#eaf3fd;
  --text:#4a4f57;
  --muted:#6b7078;
  --line:#d7dde4;
  --field:#f1f2f4;
}
*{box-sizing:border-box;margin:0;padding:0}
html,body{width:1200px;height:4506px;overflow:hidden}
body{position:relative;background:#fff;font-family:"Roboto",sans-serif;color:var(--text)}
.abs{position:absolute}
h1,h2,h3{font-family:"Inter",sans-serif;color:var(--navy)}
.btn{position:absolute;display:flex;align-items:center;justify-content:center;gap:10px;background:var(--teal);color:#fff;border-radius:30px;font-family:"Inter",sans-serif;font-weight:600;font-size:14px;letter-spacing:.2px}
.btn .dot{width:13px;height:13px;border-radius:50%;background:#fff;position:relative}
.btn .dot::after{content:"";position:absolute;left:4px;top:3.5px;border-left:5px solid var(--teal);border-top:3px solid transparent;border-bottom:3px solid transparent}
.brand{display:flex;align-items:center;gap:16px}
.brand .mark{border-radius:50%;border:3px solid var(--navy)}
.brand .name{font-family:"Inter",sans-serif;font-weight:700;color:var(--navy);line-height:1.15}
.brand .name span{display:block;font-weight:400;font-size:.62em}
.topbar{left:437px;top:0;width:763px;height:38px;background:var(--navy);border-bottom-left-radius:22px;display:flex;align-items:center;color:#fff;font-size:14px;font-family:"Inter",sans-serif}
.topbar .item{display:flex;align-items:center;gap:8px}
.social-mini{display:flex;gap:16px;margin-left:auto;margin-right:32px}
.social-mini i{width:12px;height:12px;border-radius:50%;background:#fff;display:block}
.nav{left:398px;top:64px;display:flex;gap:24px;font-family:"Inter",sans-serif;font-size:14px;font-weight:500;color:#111}
.nav .active{color:var(--teal)}
.hero-photo{left:0;top:110px;width:1200px;height:730px;background:linear-gradient(100deg,#f6f7f8 0%,#eef0f1 35%,#d9c4b6 60%,#c7d6dc 80%,#e3e8ea 100%)}
.hero h1{font-size:48px;line-height:62px;letter-spacing:-1.2px}
.hero h1 b{font-weight:800}
.hero h1 span{font-weight:400}
.about-ring{left:110px;top:841px;width:434px;height:434px;border-radius:50%;background:#fff;border:8px solid #d5d5d5}
.about-photo{left:126px;top:857px;width:402px;height:402px;border-radius:50%;background:linear-gradient(135deg,#dbe7ee,#8fc0d8 55%,#4f94b9)}
.sec-title{font-size:37px;letter-spacing:-1px}
.sec-title b{font-weight:800}
.sec-title span{font-weight:400}
.para{font-size:13.5px;line-height:24px;color:var(--text)}
.services{left:0;top:1355px;width:1200px;height:539px;background:var(--ice)}
.svc{position:absolute;width:280px}
.svc h4{font-family:"Inter",sans-serif;font-size:16px;font-weight:600;color:var(--navy);margin-bottom:12px}
.svc p{font-size:13px;line-height:20px;color:var(--muted)}
.svc.left{text-align:right}
.svc-icon{position:absolute;width:72px;height:72px;border-radius:50%;border:4px solid #fff;box-shadow:0 4px 12px rgba(22,62,99,.18);display:flex;align-items:center;justify-content:center}
.svc-icon.navy{background:var(--navy)}
.svc-icon.teal{background:var(--teal)}
.cta{left:0;top:1894px;width:1200px;height:403px;background:linear-gradient(90deg,#16476e,#1b5a82 50%,#16476e)}
.reviews{left:0;top:2935px;width:1200px;height:476px;background:linear-gradient(180deg,#2a9fa3,#238d93)}
.card{position:absolute;top:3106px;width:407px;height:229px;background:#fff;border-radius:36px}
.avatar{position:absolute;width:116px;height:116px;border-radius:50%;border:4px solid #fff;background:linear-gradient(135deg,#c9d3da,#6f8797)}
.quote{font-family:"Inter",sans-serif;font-weight:800;font-size:54px;color:var(--navy);line-height:1}
.stars{color:#f6a623;font-size:16px;letter-spacing:2px}
.field{position:absolute;height:44px;border:1px solid var(--line);background:var(--field);font-size:12px;color:var(--muted);padding:0 16px;display:flex;align-items:center;gap:8px}
.c-label{font-family:"Inter",sans-serif;font-weight:700;font-size:15px;color:#111}
.c-soc{width:32px;height:32px;border-radius:50%;background:var(--teal)}
.footer{left:0;top:4128px;width:1200px;height:378px;background:var(--navy)}
.fcol h5{font-family:"Inter",sans-serif;font-weight:600;font-size:16px;color:#fff;margin-bottom:18px}
.fcol a{display:block;color:#dbe4ee;font-size:13px;line-height:27.5px;text-decoration:none}
.f-soc{width:32px;height:32px;border-radius:50%;border:1.5px solid #fff}
.fc-item{display:flex;gap:12px;font-size:13px;color:#dbe4ee;line-height:19px;margin-bottom:14px}
.fc-item b{display:block;color:#fff;font-size:11.5px;font-weight:700}
</style>
</head>
<body>

<header>
  <div class="abs brand" style="left:112px;top:21px">
    <div class="mark" style="width:70px;height:70px"></div>
    <div class="name" style="font-size:29px">Marbleton<span>Health Group</span></div>
  </div>
  <div class="abs topbar">
    <div class="item" style="margin-left:48px">
      <svg width="14" height="14" viewBox="0 0 24 24"><path fill="#7fd3d5" d="M6.6 10.8a15 15 0 0 0 6.6 6.6l2.2-2.2c.3-.3.7-.4 1-.2 1.1.4 2.3.6 3.6.6.6 0 1 .4 1 1V20c0 .6-.4 1-1 1A17 17 0 0 1 3 4c0-.6.4-1 1-1h3.5c.6 0 1 .4 1 1 0 1.3.2 2.5.6 3.6.1.3 0 .7-.2 1z"/></svg>
      555-014-2736
    </div>
    <div class="item" style="margin-left:72px">
      <svg width="14" height="12" viewBox="0 0 24 20"><rect x="1" y="1" width="22" height="18" rx="2" fill="#7fd3d5"/><path d="M2 3l10 8 10-8" stroke="#163e63" stroke-width="2" fill="none"/></svg>
      info@marbletonhealthgroup.com
    </div>
    <div class="social-mini"><i></i><i></i><i></i></div>
  </div>
  <nav class="abs nav">
    <span class="active">Home</span><span>About Us</span><span>Our Services</span><span>Testimonials</span><span>Contact Us</span>
  </nav>
  <div class="btn" style="left:885px;top:52px;width:205px;height:46px;font-size:15px;font-weight:500">Book An Appointment</div>
</header>

<section class="hero">
  <div class="abs hero-photo" role="img" aria-label="Smiling patient talking with a doctor across a consultation desk"></div>
  <svg class="abs" style="left:0;top:640px" width="1200" height="210" viewBox="0 0 1200 210">
    <path d="M0 135 C 120 85 230 60 330 62 C 520 65 620 190 820 190 C 970 190 1100 120 1200 60 L1200 210 L0 210 Z" fill="#fff"/>
    <path d="M330 62 C 520 55 640 180 820 178 C 960 176 1100 110 1200 55 L1200 72 C 1100 140 960 200 820 195 C 640 190 520 75 330 62 Z" fill="var(--teal)"/>
  </svg>
  <h1 class="abs" style="left:111px;top:275px"><b>Modern Healthcare,</b><br><span>Designed Around You.</span></h1>
  <div class="btn" style="left:114px;top:441px;width:290px;height:47px">BOOK AN APPOINTMENT <span class="dot"></span></div>
</section>

<section>
  <div class="abs about-ring"></div>
  <div class="abs about-photo" role="img" aria-label="Smiling doctor with stethoscope in a clinic corridor, colleagues behind"></div>
  <h2 class="abs sec-title" style="left:626px;top:880px"><b>About</b> <span>Us</span></h2>
  <div class="abs para" style="left:626px;top:952px;width:464px">
    <p>Marbleton Health Group is a modern medical office focused on delivering efficient, ethical, and patient-first healthcare services. Our mission is to simplify the healthcare experience by combining professional medical care with seamless digital solutions like online appointment booking.</p>
    <p style="margin-top:18px">We believe healthcare should be accessible, transparent, and designed around the patient’s needs.</p>
  </div>
  <div class="btn" style="left:628px;top:1175px;width:184px;height:49px">LEARN MORE <span class="dot"></span></div>
</section>

<section>
  <div class="abs services"></div>
  <h2 class="abs sec-title" style="left:0;width:1200px;text-align:center;top:1395px"><b>Our</b> <span>Services</span></h2>
  <svg class="abs" style="left:0;top:1355px" width="1200" height="539">
    <g stroke="#c9d6e4" stroke-width="1.5" fill="none">
      <path d="M444 149 L500 149 L560 200"/>
      <path d="M444 284 L492 284"/>
      <path d="M444 413 L500 413 L560 360"/>
      <path d="M756 149 L700 149 L640 200"/>
      <path d="M756 284 L708 284"/>
      <path d="M756 413 L700 413 L640 360"/>
    </g>
    <circle cx="600" cy="284" r="110" fill="#fff" style="filter:drop-shadow(0 6px 14px rgba(22,62,99,.15))"/>
    <circle cx="600" cy="284" r="92" fill="none" stroke="var(--navy)" stroke-width="3"/>
    <circle cx="600" cy="284" r="40" fill="none" stroke="var(--navy)" stroke-width="3"/>
  </svg>
  <div class="svc-icon navy" style="left:372px;top:1468px"><svg width="34" height="34" viewBox="0 0 24 24" fill="none" stroke="#fff" stroke-width="1.4"><circle cx="12" cy="7" r="3"/><path d="M6 20c0-3.5 2.7-6 6-6s6 2.5 6 6"/><path d="M12 14v4M10 16h4"/></svg></div>
  <div class="svc-icon teal" style="left:372px;top:1603px"><svg width="34" height="34" viewBox="0 0 24 24" fill="none" stroke="#fff" stroke-width="1.4"><circle cx="12" cy="12" r="7"/><path d="M12 8v8M8 12h8"/></svg></div>
  <div class="svc-icon navy" style="left:372px;top:1732px"><svg width="34" height="34" viewBox="0 0 24 24" fill="none" stroke="#fff" stroke-width="1.4"><circle cx="12" cy="6" r="3"/><rect x="5" y="12" width="14" height="8" rx="1"/><path d="M9 16h6"/></svg></div>
  <div class="svc-icon teal" style="left:747px;top:1468px"><svg width="34" height="34" viewBox="0 0 24 24" fill="none" stroke="#fff" stroke-width="1.4"><rect x="4" y="4" width="16" height="16" rx="3"/><path d="M7 13h3l2-4 2 6 1-2h2"/></svg></div>
  <div class="svc-icon navy" style="left:747px;top:1603px"><svg width="34" height="34" viewBox="0 0 24 24" fill="none" stroke="#fff" stroke-width="1.4"><path d="M12 20s-7-4.5-7-10a4 4 0 0 1 7-2.5A4 4 0 0 1 19 10c0 5.5-7 10-7 10z"/></svg></div>
  <div class="svc-icon teal" style="left:747px;top:1732px"><svg width="34" height="34" viewBox="0 0 24 24" fill="none" stroke="#fff" stroke-width="1.4"><path d="M20 12a8 8 0 1 1-3-6.2"/><path d="M20 4v5h-5"/><path d="M12 9v6M9 12h6"/></svg></div>

  <div class="svc left" style="left:64px;top:1474px"><h4>Primary Care</h4><p>Lorem ipsum dolor sit amet, consectetur adipiscing elit, sed do eius</p></div>
  <div class="svc left" style="left:64px;top:1601px"><h4>Preventive Health Checkups</h4><p>Lorem ipsum dolor sit amet, consectetur adipiscing elit, sed do eius</p></div>
  <div class="svc left" style="left:64px;top:1730px"><h4>General Consultations</h4><p>Lorem ipsum dolor sit amet, consectetur adipiscing elit, sed do eius</p></div>
  <div class="svc" style="left:852px;top:1474px"><h4>Diagnostics &amp; Screenings</h4><p>Lorem ipsum dolor sit amet, consectetur adipiscing elit, sed do eius</p></div>
  <div class="svc" style="left:852px;top:1601px"><h4>Chronic Care Management</h4><p>Lorem ipsum dolor sit amet, consectetur adipiscing elit, sed do eius</p></div>
  <div class="svc" style="left:852px;top:1730px"><h4>Follow-up &amp; Ongoing Care</h4><p>Lorem ipsum dolor sit amet, consectetur adipiscing elit, sed do eius</p></div>
</section>

<section>
  <div class="abs cta" role="img" aria-label="Dimly lit clinic waiting room with sofas and plants, tinted blue"></div>
  <h2 class="abs" style="left:0;width:1200px;text-align:center;top:1973px;color:#fff;font-size:33px;line-height:47px;letter-spacing:-.8px"><b style="font-weight:700">Schedule Your Free Consultation And Let’s</b><br><span style="font-weight:400">See What We Can Create Together!</span></h2>
  <p class="abs" style="left:160px;width:880px;text-align:center;top:2084px;color:#fff;font-size:13.5px;line-height:27px">Sed ut perspiciatis unde omnis iste natus error sit voluptatem accusantium doloremque laudantium, totam rem aperiam, eaque ipsa quae ab illo inventore veritatis et quasi architecto beatae vitae dicta sunt explicabo.</p>
  <div class="abs" style="left:455px;top:2169px;width:290px;height:47px;background:#fff;border-radius:30px;display:flex;align-items:center;gap:12px;padding-left:6px;font-family:'Inter',sans-serif;font-weight:600;font-size:13px;color:var(--navy)">
    <span style="width:37px;height:37px;border-radius:50%;background:var(--teal);display:flex;align-items:center;justify-content:center"><svg width="16" height="16" viewBox="0 0 24 24"><path fill="#fff" d="M6.6 10.8a15 15 0 0 0 6.6 6.6l2.2-2.2c.3-.3.7-.4 1-.2 1.1.4 2.3.6 3.6.6.6 0 1 .4 1 1V20c0 .6-.4 1-1 1A17 17 0 0 1 3 4c0-.6.4-1 1-1h3.5c.6 0 1 .4 1 1 0 1.3.2 2.5.6 3.6.1.3 0 .7-.2 1z"/></svg></span>
    BOOK THERE FREE CONSULTATION
  </div>
</section>

<section>
  <h2 class="abs sec-title" style="left:108px;top:2443px"><b>Why</b> <span>Choose Us?</span></h2>
  <div class="abs para" style="left:110px;top:2510px;width:462px;line-height:26.5px">
    <p>Lorem ipsum dolor sit amet, consectetur adipiscing elit, sed do eiusmod tempor incididunt ut labore et dolore magna aliqua. Ut enim ad minim veniam, quis nostrud exercitation ullamco laboris nisi ut aliquip ex ea commodo consequat.</p>
    <p style="margin-top:8px">Excepteur sint occaecat cupidatat non proident, sunt in culpa qui officia deserunt mollit anim id est laborum.</p>
  </div>
  <div class="btn" style="left:110px;top:2709px;width:184px;height:49px">LEARN MORE <span class="dot"></span></div>
  <div class="abs" style="left:819px;top:2562px;width:286px;height:256px;background:var(--teal)"></div>
  <div class="abs" role="img" aria-label="Doctor in white coat writing notes on a clipboard beside a patient" style="left:647px;top:2400px;width:443px;height:400px;background:linear-gradient(135deg,#e8edea,#c9d5cf 45%,#b9a593 75%,#e9ecee)"></div>
</section>

<section>
  <div class="abs reviews" role="img" aria-label="Blurred clinic interior tinted teal"></div>
  <h2 class="abs" style="left:0;width:1200px;text-align:center;top:3015px;color:#fff;font-size:42px;letter-spacing:-1px"><b style="font-weight:800">Customer</b> <span style="font-weight:400">Reviews</span></h2>
  <svg class="abs" style="left:36px;top:3202px" width="26" height="36" viewBox="0 0 26 36"><path d="M20 4 L6 18 L20 32" stroke="#fff" stroke-width="4" fill="none"/></svg>
  <svg class="abs" style="left:1134px;top:3202px" width="26" height="36" viewBox="0 0 26 36"><path d="M6 4 L20 18 L6 32" stroke="#fff" stroke-width="4" fill="none"/></svg>

  <div class="card" style="left:168px"></div>
  <div class="avatar" role="img" aria-label="Portrait of reviewer" style="left:115px;top:3162px"></div>
  <div class="abs quote" style="left:268px;top:3134px">“</div>
  <p class="abs" style="left:270px;top:3183px;width:290px;font-size:12.5px;line-height:23px;color:var(--muted)">Sed ut perspiciatis unde omnis iste natus error sit voluptatem accusantium doloremque laudantium, totam rem aperiam,</p>
  <div class="abs" style="left:270px;top:3265px;font-family:'Inter',sans-serif;font-weight:600;font-size:16px;color:#111">Dorian Hale</div>
  <div class="abs stars" style="left:270px;top:3288px">★★★★★</div>

  <div class="card" style="left:679px"></div>
  <div class="avatar" role="img" aria-label="Portrait of reviewer" style="left:626px;top:3162px"></div>
  <div class="abs quote" style="left:779px;top:3134px">“</div>
  <p class="abs" style="left:781px;top:3183px;width:280px;font-size:12.5px;line-height:23px;color:var(--muted)">Sed ut perspiciatis unde omnis iste natus error sit voluptatem accusantium doloremque laudantium, totam rem aperiam,</p>
  <div class="abs" style="left:781px;top:3265px;font-family:'Inter',sans-serif;font-weight:600;font-size:16px;color:#111">Marisol Grant</div>
  <div class="abs stars" style="left:781px;top:3288px">★★★★★</div>
</section>

<section>
  <h2 class="abs" style="left:0;width:1200px;text-align:center;top:3480px;font-size:37px;letter-spacing:-1px"><b style="font-weight:700">contact</b> <span style="font-weight:400">Us</span></h2>
  <svg class="abs" style="left:530px;top:3530px" width="140" height="14"><path d="M2 7h38M100 7h38" stroke="var(--navy)" stroke-width="3"/><circle cx="56" cy="7" r="3.5" fill="var(--teal)"/><circle cx="70" cy="7" r="5" fill="var(--teal)"/><circle cx="84" cy="7" r="3.5" fill="var(--teal)"/></svg>

  <div class="abs" style="left:112px;top:3592px;font-family:'Inter',sans-serif;font-weight:500;font-size:20px;color:#555">Contact Details</div>
  <svg class="abs" style="left:110px;top:3652px" width="30" height="36" viewBox="0 0 24 30"><path d="M12 1a9 9 0 0 0-9 9c0 7 9 19 9 19s9-12 9-19a9 9 0 0 0-9-9z" fill="var(--teal)"/><circle cx="12" cy="10" r="3.5" fill="#fff"/></svg>
  <p class="abs" style="left:170px;top:3655px;width:330px;font-size:14px;line-height:25px">57, Lorem ipsum dolor sit amet, consectetur adipiscing elit, sed do</p>
  <svg class="abs" style="left:106px;top:3728px" width="36" height="36" viewBox="0 0 24 24" fill="none" stroke="var(--teal)" stroke-width="1.2"><path d="M6.6 10.8a15 15 0 0 0 6.6 6.6l2.2-2.2c.3-.3.7-.4 1-.2 1.1.4 2.3.6 3.6.6.6 0 1 .4 1 1V20c0 .6-.4 1-1 1A17 17 0 0 1 3 4c0-.6.4-1 1-1h3.5c.6 0 1 .4 1 1 0 1.3.2 2.5.6 3.6.1.3 0 .7-.2 1z"/><path d="M14 3a7 7 0 0 1 7 7M14 6a4 4 0 0 1 4 4"/></svg>
  <div class="abs c-label" style="left:170px;top:3733px">PHONE NUMBER</div>
  <div class="abs" style="left:170px;top:3757px;font-size:14px">+1 555 014 2736</div>
  <svg class="abs" style="left:106px;top:3805px" width="36" height="28" viewBox="0 0 36 28" fill="none" stroke="var(--teal)" stroke-width="1.8"><rect x="2" y="2" width="32" height="24" rx="1"/><path d="M2 3l16 13 16-13M2 26l12-11M34 26L22 15"/></svg>
  <div class="abs c-label" style="left:170px;top:3804px">EMAIL</div>
  <div class="abs" style="left:170px;top:3828px;font-size:14px">info@Marbleton Health group.com</div>
  <div class="abs" style="left:111px;top:3878px;display:flex;gap:10px"><span class="c-soc"></span><span class="c-soc"></span><span class="c-soc"></span></div>

  <div class="abs" style="left:560px;top:3592px;font-family:'Inter',sans-serif;font-weight:500;font-size:20px;color:#555">Get In Touch</div>
  <div class="field" style="left:560px;top:3650px;width:248px">&#9786; Name</div>
  <div class="field" style="left:840px;top:3650px;width:246px">&#9990; Phone Number</div>
  <div class="field" style="left:560px;top:3708px;width:248px">&#9993; Email Address</div>
  <div class="field" style="left:840px;top:3708px;width:246px">&#9998; Subject</div>
  <div class="field" style="left:560px;top:3766px;width:526px;height:84px;align-items:flex-start;padding-top:30px">&#9788; Messagge</div>
  <div class="btn" style="left:561px;top:3883px;width:128px;height:40px;font-weight:700">SUBMIT</div>
</section>

<footer>
  <svg class="abs" style="left:0;top:3985px" width="1200" height="150" viewBox="0 0 1200 150">
    <path d="M0 150 L0 120 C 120 70 250 10 420 8 C 620 6 700 130 880 130 C 1000 130 1120 90 1200 60 L1200 150 Z" fill="var(--navy)"/>
    <path d="M0 130 C 100 60 250 2 420 0 C 620 -2 700 110 880 112 C 1000 113 1120 70 1200 40 L1200 60 C 1120 90 1000 130 880 130 C 700 130 620 10 420 10 C 250 12 120 75 0 140 Z" fill="var(--teal)"/>
  </svg>
  <div class="abs footer"></div>
  <div class="abs brand" style="left:110px;top:4240px">
    <div class="mark" style="width:66px;height:66px;border-color:#fff"></div>
    <div class="name" style="font-size:29px;color:#fff">Marbleton<span>Health Group</span></div>
  </div>
  <div class="abs" style="left:168px;top:4338px;display:flex;gap:10px"><span class="f-soc"></span><span class="f-soc"></span><span class="f-soc"></span></div>

  <div class="abs fcol" style="left:446px;top:4202px"><h5>Quick Links</h5><a>Home</a><a>About Us</a><a>Our Services</a><a>Resources</a><a>Testimonials</a><a>Contact Us</a></div>
  <div class="abs fcol" style="left:640px;top:4202px"><h5>About Company</h5><a>Legal Information</a><a>Terms &amp; Condition</a><a>Privacy Policy</a><a>Support</a><a>Site Map</a></div>
  <div class="abs fcol" style="left:855px;top:4202px;width:250px"><h5>Contact Us</h5>
    <div class="fc-item"><span style="color:var(--teal)">&#9990;</span><div><b>Phone</b>+1 (555) 014 2736</div></div>
    <div class="fc-item"><span style="color:var(--teal)">&#9993;</span><div><b>Email</b>info@Marbleton Health group.com</div></div>
    <div class="fc-item"><span style="color:var(--teal)">&#9679;</span><div><b>Location</b>4780 W Lorem ipsum dolor sit amet, consectetur elit</div></div>
  </div>
  <div class="abs" style="left:1108px;top:4404px;width:34px;height:34px;border-radius:50%;background:var(--teal);display:flex;align-items:center;justify-content:center"><svg width="14" height="10" viewBox="0 0 14 10"><path d="M2 8l5-5 5 5" stroke="#fff" stroke-width="2" fill="none"/></svg></div>
  <div class="abs" style="left:0;width:1200px;text-align:center;top:4461px;font-size:14px;color:#dbe4ee">2026 Copyright - Marbleton Health Group | All Rights Reserved</div>
</footer>

</body>
</html>
```